blr 2014 bcard design

We have a new logo that we have yet to incorporate into any of our materials. We are under the gun to get new business cards done as soon as possible. This is our 20th year in business and we specialize in providing entertainment and audio-visual services for private and corporate events. Please see our website for more www.brasslanternrig.com
Being that we're in the entertainment industry, our "look" can be somewhat edgy and risky, but at the same time not "over the top". In fact, we would probably lean to a "less is more" style.
One side of the card should have our contact information for phones, email and address, and the other should have our slogan "Gather, Inspire, Dazzle". We also want Facebook and Instagram (brasslanternrigevents) there as well, but not sure if it should be on back or front.
Target Market(s)
High net worth individuals, creative types in both the corporate and social markets
Industry/Entity Type
Entertainment
Look and feel

```html
<!DOCTYPE html>
<html lang="en">
<head>
<meta charset="utf-8">
<title>blr business card</title>
<link href="https://fonts.googleapis.com/css2?family=Comfortaa:wght@500&family=Josefin+Sans:wght@400&family=Poppins:wght@600;700&family=Titillium+Web:ital,wght@1,900&display=swap" rel="stylesheet">
<style>
  :root {
    --backdrop: #e9e6e2;
    --card-light: #ffffff;
    --card-dark-top: #4a4a4c;
    --card-dark-bottom: #0e0e0f;
    --ink: #161616;
    --ink-light: #f4f4f4;
    --slogan: #1fa6dc;
    --accent: #7a3fc4;
  }
  * { box-sizing: border-box; margin: 0; padding: 0; }
  html, body { width: 1200px; height: 900px; overflow: hidden; }
  body {
    background: var(--backdrop);
    font-family: "Poppins", sans-serif;
    position: relative;
  }
  .card {
    position: absolute;
    top: 140px;
    width: 350px;
    height: 612px;
    border-radius: 14px;
    box-shadow: 0 10px 30px rgba(0,0,0,0.22);
    padding: 46px 26px 30px;
    display: flex;
    flex-direction: column;
  }
  .card--front { left: 210px; background: var(--card-light); color: var(--ink); }
  .card--back {
    left: 640px;
    background: linear-gradient(180deg, var(--card-dark-top), var(--card-dark-bottom));
    color: var(--ink-light);
  }
  .brand-mark {
    display: flex; align-items: center; justify-content: center; gap: 12px;
    height: 120px;
  }
  .brand-mark__dot {
    width: 26px; height: 26px; border-radius: 50%; background: var(--accent);
  }
  .brand-mark__name {
    font-family: "Poppins", sans-serif; font-weight: 700;
    font-size: 64px; color: var(--accent); line-height: 1;
  }
  .wordmark {
    margin-top: 22px;
    font-family: "Comfortaa", sans-serif; font-weight: 500;
    font-size: 32px; text-align: center; line-height: 1;
    letter-spacing: -0.5px; white-space: nowrap;
  }
  .tagline {
    margin-top: 10px;
    font-family: "Josefin Sans", sans-serif;
    font-size: 13px; letter-spacing: 3.2px; text-align: center;
    white-space: nowrap;
  }
  .slogan {
    margin-top: 24px;
    font-family: "Titillium Web", sans-serif; font-style: italic; font-weight: 900;
    font-size: 21px; color: var(--slogan); text-align: center;
    text-transform: uppercase; letter-spacing: 0.3px; white-space: nowrap;
  }
  .contact { margin-top: 24px; padding-left: 6px; list-style: none; }
  .contact__item {
    display: flex; align-items: flex-start; gap: 8px;
    font-weight: 600; font-size: 15px; line-height: 1.45;
  }
  .contact__icon { width: 15px; height: 15px; margin-top: 4px; flex: none; fill: var(--slogan); }
  .social {
    margin-top: auto;
    display: flex; align-items: center; justify-content: center; gap: 8px;
    font-weight: 700; font-size: 15px;
  }
  .social__dot { width: 12px; height: 12px; border-radius: 50%; background: var(--slogan); }
</style>
</head>
<body>
  <article class="card card--front">
    <div class="brand-mark"><span class="brand-mark__dot"></span><span class="brand-mark__name">blr</span></div>
    <h1 class="wordmark">brass lantern rig</h1>
    <p class="tagline">EVENTS &amp; ENTERTAINMENT</p>
    <p class="slogan">Gather, Inspire, Dazzle</p>
    <ul class="contact">
      <li class="contact__item">
        <svg class="contact__icon" viewBox="0 0 16 16"><path d="M3.6 1l2.4 3-1.3 1.8c.9 2 2.4 3.6 4.5 4.5L11 9l3 2.4-1.4 2.6C7 14 2 9 2 3.4z"/></svg>
        +1 212-555-0147
      </li>
      <li class="contact__item">
        <svg class="contact__icon" viewBox="0 0 16 16"><path d="M1 3h14v10H1z" /><path d="M1 3l7 6 7-6" stroke="#fff" stroke-width="1.4" fill="none"/></svg>
        info@brasslanternrig.com
      </li>
      <li class="contact__item">
        <svg class="contact__icon" viewBox="0 0 16 16"><path d="M6.5 9.5l3-3M5 7L3 9a2.8 2.8 0 004 4l2-2M11 9l2-2a2.8 2.8 0 00-4-4L7 5" stroke="#1fa6dc" stroke-width="2" fill="none"/></svg>
        www.brasslanternrig.com
      </li>
      <li class="contact__item">
        <svg class="contact__icon" viewBox="0 0 16 16"><path d="M8 1a5 5 0 015 5c0 4-5 9-5 9S3 10 3 6a5 5 0 015-5z"/><circle cx="8" cy="6" r="1.8" fill="#fff"/></svg>
        <span>48 Harbor Lane, 3rd Floor<br>Portland, ME 04101</span>
      </li>
    </ul>
    <p class="social"><span class="social__dot"></span>brasslanternrigevents</p>
  </article>

  <article class="card card--back">
    <div class="brand-mark"><span class="brand-mark__dot"></span><span class="brand-mark__name">blr</span></div>
    <h2 class="wordmark">brass lantern rig</h2>
    <p class="tagline">EVENTS &amp; ENTERTAINMENT</p>
    <p class="slogan">Gather, Inspire, Dazzle</p>
    <p class="social"><span class="social__dot"></span>brasslanternrigevents</p>
  </article>
</body>
</html>
```